"Dario Quillon" Business Card

Friends

My name is "Dario Quillon" and I need your help! I need a new business card for my personal use.

As background, "Dario Quillon" is actually an alias that I use when I meet women. Please use your creative skills to create an amazing business card for me to use!

In addition to including my name and contact details (see the "Must Have" section), you may wish to add a catchphrase or a title if you think it would help me :)

For background, please see:

http://www.dailybrightwire.com/2013/07/23/morton-feld-dario-quillon_n_5129847.html

Looking forward to seeing what you can do for me.

Hugs and kisses,

Dario Quillon [courtesy of PixelHarbor]

Target Market(s)

Adult women in New York City...or anywhere really.

Industry/Entity Type

Business

Requirements
Must have
• Please include the following details:

Dario Quillon
P: +1-555-3QUILLN
E: secrets@darioquillon-mail.com
Nice to have
• You might include a catchphrase, like "Quillon is my surname But you can call me Mr Smoothstep".

Or perhaps a title, like "Dario Quillon, Head of Sexy Times".

You're creative...I will leave the details to you my friends.
Should not have
• Any references to my actual name...because then, what's the point in using an alias?

```html
<!DOCTYPE html>
<html lang="en">
<head>
<meta charset="utf-8">
<title>Dario Quillon — Business Card</title>
<link rel="stylesheet" href="https://fonts.googleapis.com/css2?family=Michroma&family=Open+Sans:ital,wght@0,300;0,400;1,300&family=Tinos&display=swap">
<style>
  :root {
    --backdrop: #c6cacc;
    --card-black: #1c1c1c;
    --card-white: #ffffff;
    --hazard-yellow: #f4c21a;
    --stripe-yellow: #f2e11c;
    --text-light: #f2f2f2;
    --text-muted: #bdbdbd;
    --text-dark: #1c1c1c;
    --rule-grey: #cfcfcf;
  }
  * { margin: 0; padding: 0; box-sizing: border-box; }
  html, body { width: 1200px; height: 900px; overflow: hidden; }
  body { background: var(--backdrop); position: relative; font-family: "Open Sans", sans-serif; }

  .card {
    position: absolute; left: 320px; width: 560px; height: 320px;
    border-radius: 14px; overflow: hidden;
    box-shadow: 0 6px 18px rgba(0,0,0,.25);
  }
  .card--back { top: 80px; background: var(--card-black); }
  .card--front { top: 480px; background: var(--card-white); }

  /* back */
  .hazard-stripes { position: absolute; right: 0; top: 0; width: 110px; height: 320px; }
  .brand-mark { display: flex; align-items: center; gap: 12px; color: var(--text-light);
    font-family: "Michroma", sans-serif; text-transform: uppercase; }
  .brand-mark__square { width: 18px; height: 18px; background: var(--hazard-yellow); flex: none; }
  .card--back .brand-mark { position: absolute; left: 60px; top: 100px; font-size: 26px; }
  .identity { position: absolute; text-align: center; color: var(--text-light); }
  .identity__name { font-size: 13px; font-weight: 300; letter-spacing: .5px;
    text-transform: uppercase; padding-bottom: 3px; border-bottom: 1px solid var(--text-light); }
  .identity__tagline { font-size: 10px; font-style: italic; font-weight: 300; color: var(--text-muted); margin-top: 4px; }
  .card--back .identity { left: 150px; top: 170px; width: 220px; }

  /* front */
  .front__panel { position: absolute; left: 0; top: 0; width: 330px; height: 320px; background: var(--card-black); }
  .front__notch { position: absolute; left: 330px; top: 62px; width: 22px; height: 40px; }
  .card--front .brand-mark { position: absolute; left: 28px; top: 62px; font-size: 19px; }
  .card--front .identity { left: 40px; top: 128px; width: 250px; }
  .card--front .identity__name { font-size: 15px; }
  .card--front .identity__tagline { font-size: 11px; }
  .front__bands { position: absolute; left: 0; top: 212px; width: 330px; }
  .band { height: 8px; }
  .band--grey { background: #3a3a3a; height: 6px; }
  .band--yellow { background: var(--stripe-yellow); height: 8px; }
  .band--black { background: #111; height: 14px; }

  .contact { position: absolute; left: 358px; top: 48px; color: var(--text-dark); }
  .contact__name { font-family: "Michroma", sans-serif; font-size: 13px; text-transform: uppercase; margin-bottom: 5px; }
  .contact__line { font-family: "Tinos", serif; font-size: 13px; line-height: 1.3; }
  .contact__line--phone { font-weight: 700; }
  .front__emblem { position: absolute; left: 352px; top: 190px; color: var(--text-dark); }
  .card--front .front__emblem { font-size: 13px; gap: 8px; color: var(--text-dark); }
</style>
</head>
<body>

<section class="card card--back" aria-label="Card back">
  <svg class="hazard-stripes" viewBox="0 0 110 320" aria-hidden="true">
    <polygon points="22,60 110,60 110,80 18,80" fill="#f2e11c"/>
    <polygon points="30,108 110,108 110,128 26,128" fill="#f2e11c"/>
    <polygon points="34,156 110,156 110,176 30,176" fill="#f2e11c"/>
    <polygon points="30,204 110,204 110,224 26,224" fill="#f2e11c"/>
    <polygon points="22,252 110,252 110,272 18,272" fill="#f2e11c"/>
    <polygon points="14,298 110,298 110,316 10,316" fill="#f2e11c"/>
  </svg>
  <div class="brand-mark"><span class="brand-mark__square"></span>Dario Quillon</div>
  <div class="identity">
    <p class="identity__name">Dario Quillon</p>
    <p class="identity__tagline">"Part time DARIO. Full time QUILLON"</p>
  </div>
</section>

<section class="card card--front" aria-label="Card front">
  <div class="front__panel">
    <div class="brand-mark"><span class="brand-mark__square"></span>Dario Quillon</div>
    <div class="identity">
      <p class="identity__name">Dario Quillon</p>
      <p class="identity__tagline">"Part time DARIO. Full time QUILLON"</p>
    </div>
    <div class="front__bands">
      <div class="band band--grey"></div>
      <div class="band band--black"></div>
      <div class="band band--yellow"></div>
      <div class="band band--black"></div>
    </div>
  </div>
  <svg class="front__notch" viewBox="0 0 22 40" aria-hidden="true">
    <polygon points="0,0 20,20 0,40" fill="#1c1c1c"/>
  </svg>
  <div class="contact">
    <p class="contact__name">Dario Quillon</p>
    <p class="contact__line contact__line--phone">P: +1-555-3QUILLN</p>
    <p class="contact__line">E: secrets@darioquillon-mail.com</p>
  </div>
  <div class="brand-mark front__emblem"><span class="brand-mark__square"></span>Dario Quillon</div>
</section>

</body>
</html>
```